Upcoming author needs a book cover design (first in a trilogy)

I need a book cover design for my first novel. It is not yet published and I would like to present the book, complete with a cover to potential publishers. In the interim I would like to be able to use the cover as visual motivation to get it published.
The novel is called 'Any Storm, Any Harbour' and my pen name is Marisol Vey. It is a novel set in an Australian beachside town,and is about developing tenacity and courage in the face of fear - aimed at the Young adult market.
I want the cover to be text only (no images) and I really like the old school chalkboard design style. I particularly like the colours turquoise, fuschia pink and canary yellow together. As this is the first of 3 books, I would like the design, fonts and colours to be able to be stepped across all three covers...with one colour used predominently in each cover. For Any Storm, I would like the Turquoise blue to be the strongest colour.
I would like the cover to somehow reflect the fact that the story is set by and in the ocean without appearing 'cute/kitsch' at all.
Updates
Hello Designers,
Target Market(s)
Young adult readers - most books aimed here are black covers with dark print and imagery. I want this to be light, bright and really stand out on the shelves.
Industry/Entity Type
School
Requirements
Must have
- Ability to be printed out as A2
Should not have
- Images

```html
<!DOCTYPE html>
<html lang="en">
<head>
<meta charset="utf-8">
<title>Any Storm, Any Harbour — Marisol Vey</title>
<link rel="stylesheet" href="https://fonts.googleapis.com/css2?family=Rubik+Dirt&family=Cinzel:wght@400&display=swap">
<style>
  :root {
    --page: #ffffff;
    --board-base: #4a4a4a;
    --board-light: #6a6a6a;
    --board-dark: #333333;
    --chalk-dust: rgba(255, 255, 255, 0.10);
    --chalk-blue: #1414e6;
    --chalk-pink: #ee28d0;
    --canary: #f7c800;
    --corner-grey: #a8a8a8;
    --swash-white: #ffffff;
    --author-white: #ffffff;
  }
  * { margin: 0; padding: 0; box-sizing: border-box; }
  html, body {
    width: 1000px;
    height: 1200px;
    overflow: hidden;
    background: var(--page);
  }
  .canvas {
    position: relative;
    width: 1000px;
    height: 1200px;
    background: var(--page);
  }
  .cover {
    position: absolute;
    left: 166px;
    top: 66px;
    width: 704px;
    height: 1054px;
    overflow: hidden;
    background:
      radial-gradient(ellipse 260px 120px at 72% 66%, rgba(255,255,255,0.10), transparent 70%),
      radial-gradient(ellipse 300px 160px at 22% 40%, rgba(255,255,255,0.07), transparent 70%),
      radial-gradient(ellipse 340px 200px at 55% 86%, rgba(255,255,255,0.08), transparent 70%),
      radial-gradient(ellipse 220px 140px at 80% 18%, rgba(255,255,255,0.06), transparent 70%),
      radial-gradient(circle 18px at 96% 51%, rgba(0,0,0,0.35), transparent 100%),
      radial-gradient(ellipse at 50% 50%, var(--board-base) 0%, var(--board-dark) 100%);
  }
  .board-texture {
    position: absolute;
    inset: 0;
    width: 100%;
    height: 100%;
  }

  .corner-ornament {
    position: absolute;
    width: 190px;
    height: 230px;
  }
  .corner-ornament--tl { left: 0; top: 0; background: radial-gradient(ellipse at 0 0, rgba(168,168,168,0.45), rgba(168,168,168,0.12) 60%, transparent 72%); }
  .corner-ornament--tr { right: 0; top: 0; background: radial-gradient(ellipse at 100% 0, rgba(168,168,168,0.45), rgba(168,168,168,0.12) 60%, transparent 72%); }
  .corner-ornament--bl { left: 0; bottom: 0; background: radial-gradient(ellipse at 0 100%, rgba(168,168,168,0.45), rgba(168,168,168,0.12) 60%, transparent 72%); }
  .corner-ornament--br { right: 0; bottom: 0; background: radial-gradient(ellipse at 100% 100%, rgba(168,168,168,0.45), rgba(168,168,168,0.12) 60%, transparent 72%); }

  .flourish {
    position: absolute;
    left: 234px;
    width: 220px;
    height: 108px;
    background: radial-gradient(ellipse at 50% 50%, rgba(247,200,0,0.85) 0%, rgba(247,200,0,0.45) 45%, transparent 72%);
  }
  .flourish--top { top: 22px; }
  .flourish--bottom { top: 756px; }

  .divider-swash {
    position: absolute;
    left: 199px;
    top: 430px;
    width: 295px;
    height: 42px;
    background: linear-gradient(90deg, transparent 0%, rgba(255,255,255,0.9) 18%, var(--swash-white) 50%, rgba(255,255,255,0.9) 82%, transparent 100%);
    clip-path: polygon(0 70%, 20% 20%, 50% 35%, 80% 55%, 100% 15%, 85% 80%, 50% 65%, 18% 60%);
  }

  .title { font-weight: 400; font-size: inherit; }
  .title__line {
    position: absolute;
    left: 0;
    width: 100%;
    display: flex;
    align-items: center;
    justify-content: center;
    font-family: "Rubik Dirt", "Arial Black", sans-serif;
    font-weight: 400;
    line-height: 1;
    text-transform: uppercase;
    white-space: nowrap;
  }
  .title__line span { display: inline-block; }
  .title--storm { color: var(--chalk-blue); }
  .title--harbour { color: var(--chalk-pink); }

  .title__big { height: 145px; font-size: 140px; letter-spacing: -3px; }
  .title__big span { transform: scaleY(1.5); }
  .title__small { height: 72px; font-size: 84px; letter-spacing: -2px; }
  .title__small span { transform: scaleY(1.15); }
  .title__small--long { font-size: 64px; }
  .title__small--long span { transform: scaleY(1.45); }

  .title--storm .title__big { top: 149px; }
  .title--storm .title__small { top: 324px; }
  .title--harbour .title__big { top: 504px; }
  .title--harbour .title__small { top: 661px; }

  .author {
    position: absolute;
    left: 0;
    top: 862px;
    width: 100%;
    text-align: center;
    font-family: "Cinzel", "Times New Roman", serif;
    font-size: 70px;
    line-height: 1;
    letter-spacing: 1px;
    color: var(--author-white);
    text-shadow: 3px 4px 5px rgba(0,0,0,0.55);
  }
</style>
</head>
<body>
  <div class="canvas">
    <div class="cover">
      <svg class="board-texture" viewBox="0 0 704 1054" preserveAspectRatio="none" aria-hidden="true">
        <defs>
          <filter id="chalk-grain" x="0" y="0" width="100%" height="100%">
            <feTurbulence type="fractalNoise" baseFrequency="0.9" numOctaves="3" seed="4" result="noise"/>
            <feColorMatrix type="saturate" values="0" in="noise"/>
            <feComponentTransfer>
              <feFuncA type="linear" slope="0.18"/>
            </feComponentTransfer>
          </filter>
          <filter id="chalk-cloud" x="0" y="0" width="100%" height="100%">
            <feTurbulence type="fractalNoise" baseFrequency="0.008" numOctaves="3" seed="9"/>
            <feColorMatrix type="saturate" values="0"/>
            <feComponentTransfer>
              <feFuncA type="linear" slope="0.22"/>
            </feComponentTransfer>
          </filter>
        </defs>
        <rect width="704" height="1054" filter="url(#chalk-cloud)"/>
        <rect width="704" height="1054" filter="url(#chalk-grain)"/>
        <g stroke="rgba(255,255,255,0.10)" stroke-width="1.2" fill="none" stroke-linecap="round">
          <line x1="40" y1="520" x2="150" y2="470"/>
          <line x1="60" y1="760" x2="190" y2="745"/>
          <line x1="520" y1="620" x2="660" y2="600"/>
          <line x1="70" y1="640" x2="95" y2="560"/>
          <line x1="600" y1="250" x2="610" y2="330"/>
          <line x1="130" y1="880" x2="230" y2="860"/>
          <line x1="470" y1="980" x2="600" y2="1000"/>
        </g>
      </svg>

      <div class="corner-ornament corner-ornament--tl" role="img" aria-label="Grey chalk line corner ornament of petals and a small square"></div>
      <div class="corner-ornament corner-ornament--tr" role="img" aria-label="Grey chalk line corner ornament of petals and a small square"></div>
      <div class="corner-ornament corner-ornament--bl" role="img" aria-label="Grey chalk line corner ornament of petals and a small square"></div>
      <div class="corner-ornament corner-ornament--br" role="img" aria-label="Grey chalk line corner ornament of petals and a small square"></div>

      <div class="flourish flourish--top" role="img" aria-label="Canary yellow scrolled flourish ornament"></div>

      <h1 class="title title--storm">
        <span class="title__line title__big"><span>Any</span></span>
        <span class="title__line title__small"><span>Storm</span></span>
      </h1>

      <div class="divider-swash" role="img" aria-label="White calligraphic swash divider"></div>

      <h2 class="title title--harbour">
        <span class="title__line title__big"><span>Any</span></span>
        <span class="title__line title__small title__small--long"><span>Harbour</span></span>
      </h2>

      <div class="flourish flourish--bottom" role="img" aria-label="Canary yellow scrolled flourish ornament"></div>

      <p class="author">MARISOL VEY</p>
    </div>
  </div>
</body>
</html>
```